2009 Thank You

A colorful post card that is 8.5 x 5.5.  The purpose is to say thank you to our customers and to wish them a prosperous new year.  We a printing company and will print 4-color process on both sides of the post card

Requirements
Must have
• I have included our logo to be incorporated where appropriate 

Nice to have
• The theme might incorporate something that recognizes "these are turbulent times"  or "success from adversity"

```html
<!DOCTYPE html>
<html lang="en">
<head>
<meta charset="utf-8">
<title>2009 Thank You Postcard</title>
<link rel="stylesheet" href="https://fonts.googleapis.com/css2?family=Great+Vibes&family=Pinyon+Script&family=Source+Sans+3:wght@400;600&display=swap">
<style>
  :root {
    --frame-orange: #ff8a00;
    --frame-yellow: #fff200;
    --ink: #000000;
    --gold: #ffb000;
    --yellow: #fff000;
    --rule: #ffc000;
  }
  * { margin: 0; padding: 0; box-sizing: border-box; }
  html, body { width: 1200px; height: 777px; overflow: hidden; background: var(--ink); }
  .postcard {
    position: relative;
    width: 1200px;
    height: 777px;
    overflow: hidden;
    background: linear-gradient(135deg, var(--frame-orange) 0%, #ffc400 45%, var(--frame-yellow) 100%);
  }
  .postcard__field {
    position: absolute;
    left: 10px; top: 8px; right: 8px; bottom: 4px;
    background: var(--ink);
  }
  .headline {
    position: absolute;
    left: 0; top: 0;
    width: 1200px; height: 300px;
    overflow: visible;
  }
  .headline__word {
    font-family: "Great Vibes", cursive;
    font-size: 190px;
  }
  .headline__you { fill: var(--yellow); }
  .headline__rule { fill: url(#rule-fade); }
  .message {
    position: absolute;
    left: 0; width: 1200px;
    font-family: "Pinyon Script", cursive;
    font-size: 33px;
    color: var(--yellow);
    text-align: center;
    white-space: nowrap;
    line-height: 42px;
  }
  .message--thanks { top: 334px; }
  .message--wishes { top: 461px; }
  .message--call { top: 673px; }
  .contact {
    position: absolute;
    left: 107px; top: 728px;
    font-family: "Source Sans 3", sans-serif;
    font-size: 21px;
    color: var(--yellow);
    white-space: nowrap;
  }
  .brand {
    position: absolute;
    left: 1005px; top: 680px;
    width: 175px; height: 82px;
    display: flex;
    align-items: center;
    justify-content: center;
    gap: 8px;
    font-family: "Source Sans 3", sans-serif;
    font-weight: 600;
    font-size: 28px;
    color: var(--yellow);
  }
  .brand__square {
    width: 14px; height: 14px;
    background: var(--yellow);
  }
</style>
</head>
<body>
  <main class="postcard">
    <div class="postcard__field"></div>

    <svg class="headline" viewBox="0 0 1200 300" role="heading" aria-level="1" aria-label="Thank You">
      <defs>
        <linearGradient id="thank-fill" x1="0" y1="0" x2="1" y2="0">
          <stop offset="0" stop-color="#f29a1a"/>
          <stop offset="0.5" stop-color="#ffb000"/>
          <stop offset="1" stop-color="#ffd200"/>
        </linearGradient>
        <linearGradient id="rule-fade" x1="0" y1="0" x2="1" y2="0">
          <stop offset="0" stop-color="#ffc000"/>
          <stop offset="1" stop-color="#fff000"/>
        </linearGradient>
      </defs>
      <rect class="headline__rule" x="45" y="218" width="1135" height="3"/>
      <text class="headline__word headline__thank" x="170" y="195" fill="url(#thank-fill)">Thank</text>
      <text class="headline__word headline__you" x="790" y="195">You</text>
    </svg>

    <p class="message message--thanks">
      In these turbulent times it’s easy to forget that good things that are happening all around.<br>
      With this in mind, we just wanted to say thank you for your business in 2008.
    </p>

    <p class="message message--wishes">
      We hope you will enjoy a prosperous year in 2009.&nbsp;&nbsp; If there is anything we can do to help<br>
      your company succeed, please give us a call.&nbsp; We are happy to provide printing services of all<br>
      types including brochures, direct mail, multi-media campaigns to drive internet traffic, training<br>
      materials and fulfillment services.
    </p>

    <p class="message message--call">Give us a call!</p>

    <p class="contact">1720 Ridgeline Avenue | Suite #3 | Lakeview Colorado 80412 | (555) 014-2870 | www.presswellprint.com</p>

    <div class="brand">
      <span class="brand__square"></span>
      <span class="brand__name">Presswell</span>
    </div>
  </main>
</body>
</html>
```